A female friendship landing page

I need a landing page for a startup based in Toronto called Oh Petal!. The idea is basically an app that connects women with other women in their local area so that they can establish life long platonic friendships. Think of us as the Glimmo for building female friendships. The final design should promote female empowerment and female friendship. Please review the content for landing page uploaded below, as we want the text included in that document on the landing page. I have also included four images that can be used on the landing page.

Our missions: The app that connects you with other women, because life is meant for good girlfriends and great adventures.

Target Market(s)

Our target market are women between the ages of 20 and 55 living in citities

Industry/Entity Type

Startup

Coding

Coded - Design and coding required

Number of Pages Required

1 page

Font styles to use
Sans Serif
Other font styles liked:
• The font used here is nice! http://quorvel.io/

Requirements
Must have
• Atleast 2 of the pictures here:
• https://snapvault.example.com/shares/8a42c917b03e4d5fa1c6e29d7b4f0a63
• 2.The project must include sample screenshots of the app based on my description of the app! I.e I have mentioned in the content below that the we will send a personalized message to both females when there is a match. "Either search based on keywords (i.e yoga, painting, hiking) or simply swipe through suggested matches to find potential chicas. Once a match happens, we will send you both a fun “get to know you” message and customized suggestions about local places and activities that you can visit and do together. "
• So we would need a simple app screenshots (non-functional) depicting that! 2 or 3 screenshots is enough (http://quorvel.io/ has a sample screenshots of the app for its company). I would like to see Oh Petal! on the phone screenshot, at the top, as this is common.
• I really liked the following landing pages so you can use these for inspiration:
• http://quorvel.io/
• http://nestlyhub.com/
Nice to have
• The landing page should be smooth and sleek, with a feminine touch, as the website is aimed for females. It should also look simple! It should convey female friendship.
• Sample landing pages I have liked for their simple design and visible appeal. You can use these for inspiration!
• http://quorvel.io/
• http://nestlyhub.com/
• http://www.plumo-app.com/?utm_source=launchlist
Should not have
• I tried to design my own landing page : http://4qbyte.com/petal/
• and failed miserably :P Definitely do not want it looking like that!

```html
<!DOCTYPE html>
<html lang="en">
<head>
<meta charset="utf-8">
<title>Oh Petal! – Launching Soon</title>
<link rel="stylesheet" href="https://fonts.googleapis.com/css2?family=Playfair+Display:wght@400;700&family=Raleway:wght@400;500;600&display=swap">
<style>
  :root {
    --pink: #f6a5c6;
    --pink-deep: #ef7fae;
    --rose-text: #e7769f;
    --mint: #16d39a;
    --teal-ring: #8ee3cf;
    --soft-pink-ring: #f7c4d6;
    --white: #ffffff;
    --ink: #333333;
    --grey-text: #6d6d6d;
    --body-text: #555555;
    --light-bg: #f0f0f0;
    --footer-bg: #c9c9c9;
    --social: #7d7d7d;
    --dot-pink: #e486a9;
    --dot-violet: #a77cb0;
    --navy-btn: #0f2f9a;
  }
  * { box-sizing: border-box; margin: 0; padding: 0; }
  html, body { width: 1200px; height: 3279px; overflow: hidden; }
  body { position: relative; background: var(--white); font-family: "Raleway", sans-serif; color: var(--ink); }
  .section { position: absolute; left: 0; width: 1200px; }

  /* hero */
  .hero { top: 0; height: 573px; overflow: hidden; }
  .hero-photo {
    position: absolute; inset: 0;
    background:
      radial-gradient(ellipse 260px 200px at 430px 300px, rgba(214,150,110,.75), rgba(214,150,110,0) 70%),
      radial-gradient(ellipse 230px 190px at 740px 320px, rgba(200,140,100,.7), rgba(200,140,100,0) 70%),
      radial-gradient(ellipse 300px 160px at 380px 470px, rgba(160,70,60,.55), rgba(160,70,60,0) 70%),
      radial-gradient(ellipse 280px 170px at 800px 480px, rgba(150,110,50,.6), rgba(150,110,50,0) 70%),
      radial-gradient(ellipse 360px 260px at 150px 120px, rgba(190,170,60,.75), rgba(190,170,60,0) 70%),
      radial-gradient(ellipse 380px 240px at 1050px 140px, rgba(120,140,50,.7), rgba(120,140,50,0) 70%),
      radial-gradient(ellipse 300px 200px at 1100px 460px, rgba(60,40,25,.8), rgba(60,40,25,0) 70%),
      linear-gradient(180deg, #6f6a2e 0%, #5c5026 45%, #4a3320 100%);
  }
  .hero-photo::after { content: ""; position: absolute; inset: 0; background: rgba(25,18,10,.28); }
  .brand { position: absolute; top: 30px; left: 122px; font-weight: 600; font-size: 24px; color: var(--pink); }
  .menu-btn { position: absolute; top: 30px; left: 1109px; width: 35px; height: 35px; border-radius: 50%; background: rgba(255,255,255,.35); }
  .menu-btn span { position: absolute; left: 10px; width: 15px; height: 2px; background: var(--white); }
  .hero-title { position: absolute; top: 128px; left: 0; width: 1200px; text-align: center; font-family: "Playfair Display", serif; font-weight: 700; font-size: 54px; color: var(--white); }
  .hero-sub { position: absolute; top: 218px; left: 290px; width: 620px; text-align: center; font-size: 15px; line-height: 21px; color: var(--white); }
  .hero-launch { position: absolute; top: 368px; left: 0; width: 1200px; text-align: center; font-family: "Playfair Display", serif; font-weight: 700; font-size: 52px; color: var(--white); }
  .btn { position: absolute; width: 352px; height: 51px; background: var(--pink); color: var(--white); font-size: 21px; text-align: center; line-height: 51px; letter-spacing: .5px; }
  .hero .btn { top: 455px; left: 428px; }

  /* phone */
  .phone { position: absolute; background: var(--white); border: 2px solid #dcdcdc; border-radius: 34px; box-shadow: 0 10px 30px rgba(0,0,0,.2); }
  .phone .speaker { position: absolute; top: 5.5%; left: 40%; width: 20%; height: 5px; border-radius: 3px; background: #bdbdbd; }
  .phone .camera { position: absolute; top: 4.8%; left: 30%; width: 9px; height: 9px; border-radius: 50%; background: #222; }
  .phone .screen { position: absolute; top: 11.5%; left: 5.5%; right: 5.5%; bottom: 12.5%; overflow: hidden; }
  .phone .home { position: absolute; bottom: 3%; left: 50%; width: 40px; height: 40px; margin-left: -20px; border-radius: 50%; border: 2px solid #bdbdbd; }
  .phone.gold { border-color: #e0c9a8; }
  .screen.pink { background: var(--pink); }
  .app-mark { position: absolute; left: 50%; width: 110px; height: 56px; margin-left: -55px; background: var(--white); border-radius: 28px; text-align: center; line-height: 56px; font-weight: 600; font-size: 18px; color: var(--pink-deep); }
  .app-line { position: absolute; top: 0; width: 2px; background: var(--white); }

  /* side dots */
  .dots { position: absolute; left: 1157px; width: 10px; }
  .dots i { display: block; width: 10px; height: 10px; border-radius: 50%; background: var(--dot-pink); margin-bottom: 9px; }
  .dots i.on { background: var(--dot-violet); }
  .dots.light i { background: #eab1c6; }

  /* about */
  .about { top: 704px; height: 713px; background: var(--mint); }
  .about-doodles { position: absolute; top: 90px; left: 160px; width: 400px; height: 460px; background: radial-gradient(ellipse at center, rgba(20,110,80,.18), rgba(20,110,80,0) 70%); }
  .like-label { position: absolute; top: 44px; width: 100%; text-align: center; font-size: 14px; color: #c9c9c9; }
  .choice { position: absolute; left: 50%; width: 150px; height: 150px; margin-left: -75px; border-radius: 50%; border: 2px solid; text-align: center; line-height: 146px; font-size: 19px; color: #d3d3d3; }
  .choice.coffee { top: 86px; border-color: var(--soft-pink-ring); }
  .choice.wine { top: 166px; border-color: var(--teal-ring); background: rgba(255,255,255,.6); }
  .with { position: absolute; top: 150px; width: 100%; text-align: center; font-size: 9px; color: #cfcfcf; z-index: 1; }
  .about-copy { position: absolute; top: 196px; left: 621px; width: 408px; font-size: 14.5px; line-height: 32px; color: var(--white); text-align: justify; }
  .about-copy mark { background: var(--pink); color: var(--white); padding: 1px 3px; }

  /* how it works */
  .how { top: 1417px; height: 719px; }
  .step { position: absolute; width: 280px; font-size: 11.5px; line-height: 20px; color: var(--body-text); }
  .step h3 { font-family: "Playfair Display", serif; font-weight: 700; font-size: 12.5px; color: var(--rose-text); margin-bottom: 2px; }
  .screen.photo {
    background:
      radial-gradient(ellipse 70px 120px at 80px 230px, rgba(70,60,80,.55), rgba(70,60,80,0) 75%),
      radial-gradient(ellipse 60px 110px at 175px 200px, rgba(60,55,75,.5), rgba(60,55,75,0) 75%),
      radial-gradient(ellipse 200px 90px at 130px 400px, rgba(240,232,200,.9), rgba(240,232,200,0) 75%),
      linear-gradient(180deg, #9fc3bf 0%, #c2d2c8 40%, #dcdcc6 70%, #efeadb 100%);
  }
  .signin { position: absolute; left: 12px; right: 12px; top: 365px; height: 38px; background: var(--navy-btn); color: var(--white); font-size: 17px; text-align: center; line-height: 38px; }
  .slider-dots { position: absolute; top: 2089px; left: 574px; }
  .slider-dots i { float: left; width: 6px; height: 6px; border-radius: 50%; background: #8a7a86; margin-right: 11px; }
  .slider-dots i.on { background: #c0657f; }

  /* quote */
  .quote { top: 2136px; height: 424px; overflow: hidden; }
  .quote-photo {
    position: absolute; inset: 0;
    background:
      radial-gradient(ellipse 260px 150px at 120px 60px, rgba(110,140,190,.8), rgba(110,140,190,0) 70%),
      radial-gradient(ellipse 220px 120px at 1100px 40px, rgba(120,150,190,.6), rgba(120,150,190,0) 70%),
      radial-gradient(ellipse 240px 230px at 400px 220px, rgba(225,190,140,.85), rgba(225,190,140,0) 70%),
      radial-gradient(ellipse 250px 230px at 700px 200px, rgba(235,205,160,.85), rgba(235,205,160,0) 70%),
      radial-gradient(ellipse 200px 180px at 560px 360px, rgba(190,120,110,.6), rgba(190,120,110,0) 70%),
      radial-gradient(ellipse 260px 200px at 1000px 340px, rgba(50,40,40,.8), rgba(50,40,40,0) 70%),
      linear-gradient(100deg, #6b6e80 0%, #9a8370 35%, #b39477 55%, #7a6358 78%, #3f3738 100%);
  }
  .quote-photo::after { content: ""; position: absolute; inset: 0; background: rgba(30,20,25,.38); }
  .quote-text { position: absolute; top: 185px; left: 0; width: 1200px; text-align: center; font-family: "Playfair Display", serif; font-size: 33px; line-height: 64px; color: var(--white); }

  /* subscribe */
  .subscribe { top: 2560px; height: 638px; background: var(--light-bg); overflow: hidden; }
  .subscribe h2 { position: absolute; top: 68px; width: 1200px; text-align: center; font-family: "Playfair Display", serif; font-weight: 700; font-size: 60px; color: var(--ink); }
  .subscribe p { position: absolute; top: 155px; width: 1200px; text-align: center; font-family: "Playfair Display", serif; font-size: 25px; color: var(--grey-text); }
  .subscribe .btn { top: 216px; left: 428px; }
  .doodles { position: absolute; top: 365px; left: 420px; width: 360px; height: 180px; background: radial-gradient(ellipse at center, rgba(180,180,180,.35), rgba(240,240,240,0) 70%); }

  /* footer */
  .footer { top: 3198px; height: 81px; background: var(--footer-bg); }
  .social { position: absolute; top: 26px; width: 30px; height: 30px; border-radius: 50%; background: var(--social); }
  .copyright { position: absolute; top: 33px; left: 870px; width: 220px; text-align: right; font-size: 10px; color: #666; }
</style>
</head>
<body>

<section class="section hero">
  <div class="hero-photo" role="img" aria-label="Photo of two smiling women sharing coffee outdoors in autumn"></div>
  <div class="brand">Oh Petal!</div>
  <div class="menu-btn"><span style="top:11px"></span><span style="top:16px"></span><span style="top:21px"></span></div>
  <h1 class="hero-title">There is no place like friendship</h1>
  <p class="hero-sub">The app that connects you with other women, because life is meant for good girlfriends and great adventures.</p>
  <div class="hero-launch">Launching Soon</div>
  <div class="btn">SUBSCRIBE NOW</div>
  <div class="dots" style="top:347px"><i class="on"></i><i></i><i></i><i></i><i></i></div>
</section>

<div class="phone" style="left:872px;top:298px;width:190px;height:396px;z-index:2">
  <span class="camera"></span><span class="speaker"></span>
  <div class="screen pink">
    <span class="app-line" style="left:22px;height:170px"></span>
    <div class="app-mark" style="top:166px">Oh Petal!</div>
  </div>
  <span class="home"></span>
</div>

<section class="section about">
  <div class="about-doodles" role="img" aria-label="Faint line doodles of hats, sunglasses, drinks and mittens"></div>
  <div class="phone gold" style="left:240px;top:79px;width:237px;height:551px">
    <span class="camera"></span><span class="speaker"></span>
    <div class="screen" style="background:#fff">
      <div class="like-label">I like meeting up for...</div>
      <div class="choice coffee">Coffee</div>
      <div class="with">with</div>
      <div class="choice wine">Wine</div>
    </div>
    <span class="home"></span>
  </div>
  <p class="about-copy"><mark>Oh Petal!</mark> is the app that empowers women to meet other lovely women. We help you meet women you wouldn't have otherwise met conventionally. We understand that it's not always easy to make friends, and over time it's natural to get set in your ways. Oh Petal! helps you break out of that routine and get into new adventures with fun women. Whether you want to expand your social or professional circle, or you're looking to meet a girlfriend who is passionate about the outdoors, or the latest fitness craze, we help you build the foundation for a strong and nurturing friendship.</p>
  <div class="dots light" style="top:290px"><i></i><i></i><i></i><i></i><i></i></div>
</section>

<section class="section how">
  <div class="step" style="left:114px;top:143px">
    <h3>Create your own profile or Log in with Chatterly</h3>
    Connect with other wonderful chicas in your local area
  </div>
  <div class="step" style="left:114px;top:346px">
    <h3>Search, Swipe &amp; Match</h3>
    Either search based on keywords (i.e yoga, painting, hiking) or simply swipe through suggested matches to find potential chicas. Once a match happens, we will send you both a fun "get to know you" message and customized suggestions about local places and activities that you can visit and do together.
  </div>
  <div class="phone" style="left:463px;top:59px;width:287px;height:579px">
    <span class="camera"></span><span class="speaker"></span>
    <div class="screen photo" role="img" aria-label="Blurred photo of two friends jumping for joy against the sky">
      <div class="signin">Sign In with Chatterly</div>
    </div>
    <span class="home"></span>
  </div>
  <div class="step" style="left:815px;top:147px">
    <h3>Tell us a little about yourself!</h3>
    We connect you with other women based on your hobbies, interests, location, age preference and life stage. You may be a woman in her mid-twenties looking to meet other girls her age, or maybe you love to bake and want a baking buddy, or you recently had a kid and want to connect with other new moms. Here at Oh Petal! you can do just that! Gone are the days of wishing and here are the days of doing!
  </div>
  <div class="step" style="left:815px;top:374px">
    <h3>Meet &amp; Greet!</h3>
    Once you've had a chance to chat with your new sista, make plans, and meet her in person, because this is the beginning of a beautiful friendship.
  </div>
  <div class="dots" style="top:241px"><i></i><i></i><i></i><i></i><i></i></div>
</section>
<div class="slider-dots"><i class="on"></i><i></i><i></i><i></i></div>

<section class="section quote">
  <div class="quote-photo" role="img" aria-label="Photo of two laughing friends in sunglasses on a road trip"></div>
  <p class="quote-text">“Make your destiny out of the friendships you grow,<br>and then make it a better world around you”</p>
  <div class="dots" style="top:140px"><i></i><i></i><i></i><i></i><i></i></div>
</section>

<section class="section subscribe">
  <h2>Launching Soon</h2>
  <p>Subscribe so you are the first to be notified when Oh Petal! launches !</p>
  <div class="btn">SUBSCRIBE NOW</div>
  <div class="doodles" role="img" aria-label="Faint line doodles of accessories, drinks and outdoor items"></div>
  <div class="phone" style="left:503px;top:439px;width:192px;height:320px;border-radius:30px 30px 0 0;box-shadow:none">
    <span class="camera" style="top:26px"></span><span class="speaker" style="top:29px"></span>
    <div class="screen pink" style="top:54px;bottom:0">
      <span class="app-line" style="left:22px;height:40px"></span>
      <div class="app-mark" style="top:38px">Oh Petal!</div>
    </div>
  </div>
  <div class="dots" style="top:264px"><i></i><i></i><i></i><i></i><i class="on"></i></div>
</section>

<footer class="section footer">
  <span class="social" style="left:130px"></span>
  <span class="social" style="left:181px"></span>
  <span class="social" style="left:233px"></span>
  <span class="social" style="left:285px"></span>
  <p class="copyright">All Rights Reserved. Copyrights @ ohpetal.com</p>
</footer>

</body>
</html>
```